Thermostat Screen Design

We need a screen layout design for a new thermostat we're currently developing. If you're not familiar with thermostats, you can see some examples here - http://heating-dials-compared.bestlistguide.example/

We're after the main page design, with icons, colours etc. It needs to be clean, modern and minimalistic. Attached is all components required on the screen. The screen size is 5 inch (diagnol).

The arrows on the screen showcase what happens when you press a button. For example, when you press MODE once you get OFF, press it twice, HEAT, press it 3 times, COOL, etc. This is just for your reference.

You have complete creative license on how you choose to layout the screen, position the components etc, but we require:

- it must be on a 5 inch screen diagnol
- modern, clean and minimalistic
- includes icons and colours
- Intuitive

Let me know if any questions.

```html
<!DOCTYPE html>
<html lang="en">
<head>
<meta charset="utf-8">
<title>Thermostat Main Screen</title>
<link rel="stylesheet" href="https://fonts.googleapis.com/css2?family=Arimo:wght@400;700&display=swap">
<style>
  :root {
    --frame: #171717;
    --screen-core: #1c6874;
    --screen-edge: #07262d;
    --panel: rgba(52, 178, 186, 0.38);
    --button-top: #1592d2;
    --button-bottom: #064a72;
    --room-top: #108fd6;
    --room-bottom: #0a6fae;
    --setpoint: #0f93e6;
    --pill: rgba(8, 84, 112, 0.85);
    --chip: rgba(228, 234, 238, 0.9);
    --chip-text: #2c3338;
    --accent-blue: #1b7fcc;
    --white: #ffffff;
  }
  * { box-sizing: border-box; margin: 0; padding: 0; }
  html, body { width: 1200px; height: 1065px; overflow: hidden; background: var(--frame); }
  body { font-family: "Arimo", Arial, sans-serif; color: var(--white); }

  .thermostat { position: relative; width: 1200px; height: 1065px; background: var(--frame); }
  .screen {
    position: absolute; left: 38px; top: 39px; width: 1122px; height: 986px;
    background: radial-gradient(ellipse at 58% 50%, var(--screen-core) 0%, #0f4450 55%, var(--screen-edge) 100%);
    border: 1px solid #0c2a30;
  }

  /* side menu */
  .menu-button {
    position: absolute; left: 83px; width: 162px; height: 136px; border-radius: 16px;
    background: linear-gradient(180deg, var(--button-top) 0%, #0a6ea5 45%, var(--button-bottom) 100%);
    box-shadow: 0 4px 10px rgba(0,0,0,0.35);
    text-align: center; font-weight: 700; font-size: 24px; padding-top: 14px;
  }
  .menu-button svg { display: block; margin: 8px auto 0; }
  .menu-mode { top: 110px; }
  .menu-fan { top: 299px; }
  .menu-zone { top: 488px; }
  .menu-settings { top: 677px; }

  /* clock tab */
  .clock {
    position: absolute; left: 462px; top: 85px; width: 455px; height: 130px;
    border-radius: 30px 30px 0 0;
    background: linear-gradient(180deg, #1b8fd0 0%, rgba(14, 110, 168, 0.7) 100%);
    text-align: center;
  }
  .clock-time { font-weight: 700; font-size: 58px; line-height: 1; margin-top: 18px; letter-spacing: 1px; }
  .clock-time span { font-size: 31px; margin-left: 6px; }
  .clock-date { font-weight: 700; font-size: 31px; margin-top: 4px; }

  /* central panel */
  .main-panel {
    position: absolute; left: 293px; top: 243px; width: 805px; height: 645px;
    border-radius: 105px; background: var(--panel);
  }

  .readings { position: absolute; left: 388px; top: 284px; width: 610px; height: 86px; }
  .readings svg { position: absolute; left: 0; top: 0; }
  .reading-outdoor { position: absolute; left: 0; top: 8px; width: 210px; text-align: center; }
  .reading-indoor { position: absolute; left: 222px; top: 8px; width: 390px; text-align: center; }
  .reading-label { font-size: 25px; color: var(--chip-text); line-height: 1.1; }
  .reading-value { color: var(--accent-blue); line-height: 1.05; }
  .reading-outdoor .reading-value { font-size: 46px; }
  .reading-indoor .reading-value { font-size: 39px; font-weight: 700; }

  .room-card {
    position: absolute; left: 362px; top: 450px; width: 362px; height: 358px; border-radius: 32px;
    background: linear-gradient(180deg, var(--room-top) 0%, var(--room-bottom) 100%);
    box-shadow: 0 6px 16px rgba(0,0,0,0.25);
  }
  .room-label { position: absolute; left: 0; width: 100%; top: 24px; text-align: center; font-size: 48px; }
  .room-temp { position: absolute; left: 0; width: 100%; top: 88px; text-align: center; font-size: 140px; font-weight: 700; line-height: 1; }
  .room-status { position: absolute; left: 63px; top: 270px; font-size: 25px; font-weight: 700; line-height: 1.25; white-space: pre; }

  .mode-pill {
    position: absolute; height: 50px; border-radius: 25px; background: var(--pill);
    font-size: 37px; font-weight: 700; text-align: center; line-height: 52px;
  }
  .pill-heat { left: 748px; top: 497px; width: 194px; }
  .pill-cool { left: 753px; top: 706px; width: 184px; }

  .setpoint {
    position: absolute; left: 775px; top: 567px; width: 139px; height: 117px;
    border-radius: 8px 18px 8px 24px; background: var(--setpoint);
    font-size: 60px; font-weight: 700; text-align: center; line-height: 117px;
  }
  .adjust { position: absolute; left: 964px; }
  .adjust-up { top: 489px; }
  .adjust-down { top: 698px; }

  .tab {
    position: absolute; top: 920px; height: 74px; border-radius: 16px 16px 0 0;
    background: linear-gradient(180deg, rgba(10, 96, 122, 0.9), rgba(8, 70, 90, 0.6));
    font-size: 38px; font-weight: 700; text-align: center; line-height: 76px;
  }
  .tab-sleep { left: 477px; width: 198px; }
  .tab-zone { left: 696px; width: 213px; }
</style>
</head>
<body>
<div class="thermostat">
  <div class="screen" role="img" aria-label="Dark teal textured screen background"></div>

  <div class="menu-button menu-mode">MODE
    <svg width="90" height="90" viewBox="0 0 90 90" aria-hidden="true">
      <path d="M72 44 A29 29 0 1 1 56 18" fill="none" stroke="#fff" stroke-width="9" stroke-linecap="round"/>
      <polygon points="58,38 86,38 72,60" fill="#fff" transform="rotate(-25 72 46)"/>
    </svg>
  </div>
  <div class="menu-button menu-fan">FAN
    <svg width="96" height="96" viewBox="0 0 96 96" aria-hidden="true">
      <g fill="#fff">
        <path d="M44 40 C30 20 4 26 4 40 C4 52 26 52 44 48 Z"/>
        <path d="M52 40 C62 22 90 14 90 30 C90 44 68 46 54 48 Z"/>
        <path d="M44 54 C36 70 44 92 58 90 C70 88 62 66 54 54 Z"/>
        <circle cx="49" cy="47" r="10"/>
      </g>
      <circle cx="49" cy="47" r="4" fill="#0a6ea5"/>
    </svg>
  </div>
  <div class="menu-button menu-zone">ZONE
    <svg width="84" height="84" viewBox="0 0 84 84" aria-hidden="true">
      <rect x="6" y="6" width="72" height="72" fill="none" stroke="#fff" stroke-width="8" stroke-dasharray="14 6"/>
    </svg>
  </div>
  <div class="menu-button menu-settings">SETTINGS
    <svg width="90" height="90" viewBox="0 0 90 90" aria-hidden="true">
      <g fill="#fff" transform="translate(45 45)">
        <rect x="-9" y="-42" width="18" height="84" rx="3"/>
        <rect x="-9" y="-42" width="18" height="84" rx="3" transform="rotate(45)"/>
        <rect x="-9" y="-42" width="18" height="84" rx="3" transform="rotate(90)"/>
        <rect x="-9" y="-42" width="18" height="84" rx="3" transform="rotate(135)"/>
        <circle r="32"/>
      </g>
      <circle cx="45" cy="45" r="17" fill="#0a6ea5"/>
    </svg>
  </div>

  <div class="clock">
    <div class="clock-time">08:35<span>PM</span></div>
    <div class="clock-date">Sunday, March-17-2014</div>
  </div>

  <div class="main-panel"></div>

  <div class="readings">
    <svg width="612" height="86" viewBox="0 0 612 86" aria-hidden="true">
      <path d="M8 0 H237 L197 86 H8 A8 8 0 0 1 0 78 V8 A8 8 0 0 1 8 0 Z" fill="rgba(228,234,238,0.9)"/>
      <path d="M254 0 H602 A8 8 0 0 1 610 8 V78 A8 8 0 0 1 602 86 H216 Z" fill="rgba(228,234,238,0.9)"/>
    </svg>
    <div class="reading-outdoor">
      <div class="reading-label">OUTDOOR</div>
      <div class="reading-value">22°</div>
    </div>
    <div class="reading-indoor">
      <div class="reading-label">INDOOR RH</div>
      <div class="reading-value">45% Humidity</div>
    </div>
  </div>

  <div class="room-card">
    <div class="room-label">ROOM</div>
    <div class="room-temp">18°</div>
    <div class="room-status">SLEEEP : 60 MIN
MODE    : AUTO</div>
  </div>

  <div class="mode-pill pill-heat">HEAT</div>
  <div class="setpoint">21°</div>
  <div class="mode-pill pill-cool">COOL</div>

  <svg class="adjust adjust-up" width="78" height="66" viewBox="0 0 78 66" aria-label="Raise temperature" role="img">
    <defs>
      <linearGradient id="up-fill" x1="0" y1="0" x2="0" y2="1">
        <stop offset="0" stop-color="#1e8fe0"/><stop offset="1" stop-color="#0a4e78"/>
      </linearGradient>
    </defs>
    <polygon points="39,0 78,66 0,66" fill="url(#up-fill)"/>
  </svg>
  <svg class="adjust adjust-down" width="78" height="66" viewBox="0 0 78 66" aria-label="Lower temperature" role="img">
    <defs>
      <linearGradient id="down-fill" x1="0" y1="0" x2="0" y2="1">
        <stop offset="0" stop-color="#ffffff"/><stop offset="1" stop-color="#a9c4cc"/>
      </linearGradient>
    </defs>
    <polygon points="0,0 78,0 39,66" fill="url(#down-fill)"/>
  </svg>

  <div class="tab tab-sleep">SLEEP</div>
  <div class="tab tab-zone">ZONE 1</div>
</div>
</body>
</html>
```